Brochure Design - Non-Profit Fundraising Stream

We are a non-profit organization that is developing a fundraising project through the donation of life insurance policies. We have three brochures in each English and French that we developed for a sister organization that we want to reintegrate with our Foundation, keeping the same copy text just changing the logos, colors and make it overall more visually appealing. The foundation is called the 'Varnek-Holt Syndrome Foundation Canada'.
The original files in .docx format are attached as is the full logo and two symbol files. The deliverables would be six documents in total (InDesign or .docx), each brochure in English and French. The color hex codes are:
red: #7b2850
dark blue: #2c79a7
pale blue: #78b2e2

```html
<!DOCTYPE html>
<html lang="en">
<head>
<meta charset="utf-8">
<title>Varnek-Holt Syndrome Foundation Canada – Policy Donation Q&amp;A</title>
<link rel="stylesheet" href="https://fonts.googleapis.com/css2?family=Fira+Sans:wght@400;600;700&display=swap">
<style>
  :root {
    --backdrop: #c5c7d3;
    --paper: #fafafa;
    --ink: #1a1a1a;
    --header-blue: #2a6e9c;
    --brand-blue: #2c79a7;
    --pale-blue: #78b2e2;
    --row-tint: #c9e6f8;
    --rule: #6fa9d6;
    --frame: #1f2a36;
  }
  * { box-sizing: border-box; margin: 0; padding: 0; }
  html, body {
    width: 1200px; height: 800px; overflow: hidden;
    background: var(--backdrop);
    font-family: "Fira Sans", Arial, sans-serif;
    color: var(--ink);
  }
  .sheet {
    position: absolute; left: 325px; top: 10px;
    width: 550px; height: 780px;
    background: var(--paper);
    padding: 31px 33px 0;
  }
  .sheet-head {
    display: flex; justify-content: space-between; align-items: flex-start;
    height: 56px;
  }
  .sheet-title {
    font-weight: 700; font-size: 21.5px; line-height: 26px;
    letter-spacing: -0.1px;
  }
  .brand-mark {
    display: flex; align-items: center; gap: 6px;
    margin-top: 8px;
    font-size: 18px; font-weight: 400; color: var(--brand-blue);
  }
  .brand-mark svg { display: block; }
  .qa-table {
    width: 484px; border-collapse: collapse;
    border: 1px solid var(--frame);
    font-size: 9.9px; line-height: 12.2px;
  }
  .qa-table th {
    background: var(--header-blue); color: #fff;
    font-weight: 400; text-align: left; text-transform: uppercase;
    height: 18px; padding: 0 12px; font-size: 9.9px;
  }
  .qa-table th + th { border-left: 1px solid var(--frame); }
  .qa-table td {
    padding: 0 12px; vertical-align: middle;
    border-top: 1px solid var(--rule);
  }
  .qa-table td.question { width: 201px; border-right: 1px solid var(--frame); }
  .qa-table tbody tr:nth-child(even) td { background: var(--row-tint); }
  .qa-table ul { list-style: none; }
  .qa-table li { padding-left: 13px; position: relative; }
  .qa-table li::before {
    content: ""; position: absolute; left: 2px; top: 5px;
    width: 3px; height: 3px; background: var(--ink);
  }
  .qa-table li li { padding-left: 13px; }
  .qa-table li li::before { border-radius: 50%; left: 13px; }
  .qa-table li li { margin-left: 0; padding-left: 26px; margin-left: -13px; }
  .total { font-weight: 600; }
  .contact-line {
    text-align: center; font-size: 15.5px; margin-top: 9px;
  }
</style>
</head>
<body>
  <article class="sheet">
    <header class="sheet-head">
      <h1 class="sheet-title">Varnek-Holt Syndrome<br>Foundation Canada</h1>
      <div class="brand-mark">
        <span>Varnek-Holt</span>
        <svg width="14" height="14" viewBox="0 0 14 14" aria-hidden="true"><circle cx="7" cy="7" r="6" fill="var(--pale-blue)"/></svg>
      </div>
    </header>

    <table class="qa-table">
      <thead>
        <tr><th>Questions</th><th>Answers</th></tr>
      </thead>
      <tbody>
        <tr style="height:21px"><td class="question">What types of policies are eligible?</td><td>Term/permanent (whole life and universal)</td></tr>
        <tr style="height:21px"><td class="question">Who pays for medical underwriting?</td><td>The Foundation</td></tr>
        <tr style="height:21px"><td class="question">Who pays for actuarial underwriting?</td><td>The Foundation</td></tr>
        <tr style="height:21px"><td class="question">What size policies do you accept?</td><td>Between $50k and $10m</td></tr>
        <tr style="height:63px"><td class="question">What are your selection criteria?</td><td>We are working with a life expectancy (LE) calculation of up to 5 years. However, depending upon the circumstances we could go beyond 5 years. Rule of thumb: insured is 70 years old and over, with a medical condition or 80 years old and over, without medical condition.</td></tr>
        <tr style="height:26px"><td class="question">Who pays the premiums after the policy has been donated?</td><td>The Foundation</td></tr>
        <tr style="height:27px"><td class="question">Who is the beneficiary of the policy after it has been donated?</td><td>The Foundation</td></tr>
        <tr style="height:26px"><td class="question">Who is the owner after the policy has been donated?</td><td>The Foundation</td></tr>
        <tr style="height:27px"><td class="question">Who does all of the due diligence and underwriting?</td><td>The foundation has partnered with Calloway Charity Services who looks after these aspects.</td></tr>
        <tr style="height:114px"><td class="question">How does the process work?</td><td>You call/email us and give us the following information:
          <ul>
            <li>Face value of the policy</li>
            <li>Annual premium (current and renewal)</li>
            <li>Type of policy
              <ul><li>If term, is it convertible without medical underwriting?</li></ul>
            </li>
            <li>Policy expiration</li>
            <li>Medical condition(s) of the insured</li>
            <li>Age of the insured</li>
          </ul></td></tr>
        <tr style="height:31px"><td class="question">How long does the policy have to have been in force for?</td><td>The policy must be in force for over 2 years.</td></tr>
        <tr style="height:63px"><td class="question">How long does the process take?</td><td>Triage: less than a week<br>Medical underwriting: 1-2 weeks<br>Actuarial underwriting: 1 week<br>Donation paperwork: 1 day<br><span class="total">Total time: 3-4 weeks</span></td></tr>
        <tr style="height:31px"><td class="question">What is the typical value of the tax receipt that the donor will receive?</td><td>It varies on the life expectancy calculation, which depends on age and medical situation.</td></tr>
        <tr style="height:31px"><td class="question">What if one of my relatives wanted to benefit from the policy?</td><td>Before a policy donation is approved, we must ensure that no relative is interested in taking over the policy.</td></tr>
        <tr style="height:32px"><td class="question">Is it legal?</td><td>Yes; the entire process is legal, ethical, and approved by the government.</td></tr>
        <tr style="height:50px"><td class="question">But what’s in it for me?</td><td>You had planned to cancel your policy in order to save paying the premiums. The Foundation pays the premiums (you save $$) and you get a tax receipt (good for 5 years) which puts money back into your pocket.</td></tr>
      </tbody>
    </table>

    <p class="contact-line">+1-844-555-0172 (Toll Free) | info@varnekholtcanada.org</p>
  </article>
</body>
</html>
```